Existing WP site needs a fresh look (design only)

The current website, www.tarnbelle.com.au, is fine, but needs a fresh look so their clients can tell their website has been 'refreshed' regularly.
https://www.tarnbelle.com.au/sitemap/
They will use the existing functionality.
They want to keep the blue, green and white of their logo as the main colors, but a fresh look. They prefer a light look to a dark look, but they would be open to good designs that change their mind.
Be creative, think outside the box.
You only need to supply the 'home page ' design to win but the winners will be asked to provide an extra 'standard' page template (like the one currently being used for search results and other pages)
Any photos used must be supplied without charge with the PSDs in a resolution acceptable for the WordPress site.
2 page

```html
<!DOCTYPE html>
<html lang="en">
<head>
<meta charset="utf-8">
<title>Tarnbelle Voices – Home</title>
<link href="https://fonts.googleapis.com/css2?family=Nunito+Sans:wght@400;600;700;800&display=swap" rel="stylesheet">
<style>
:root{
  --navy:#1a3a5b;
  --navy-deep:#17344f;
  --green:#7cbb2a;
  --green-dark:#3f8a3f;
  --light:#eef4fb;
  --text:#1f2f40;
  --muted:#5c6b78;
  --white:#fff;
}
*{box-sizing:border-box;margin:0;padding:0}
html,body{width:1200px;height:3158px;overflow:hidden}
body{position:relative;font-family:"Nunito Sans",sans-serif;color:var(--text);background:var(--white)}
.abs{position:absolute}
/* hero */
.hero-dark{left:0;top:0;width:713px;height:563px;background:var(--navy)}
.hero-light{left:713px;top:0;width:487px;height:563px;background:var(--light)}
.contact-bar{left:463px;top:0;width:587px;height:37px;background:var(--green);clip-path:polygon(0 0,100% 0,100% 100%,45px 100%);color:var(--white);font-size:13px}
.contact-bar span{position:absolute;top:10px;display:flex;align-items:center;gap:10px}
.contact-bar svg{width:15px;height:15px}
.logo{display:flex;align-items:center;gap:8px;color:var(--white);font-weight:800;font-size:22px;letter-spacing:1px}
.logo i{width:16px;height:16px;background:var(--green);display:block}
.nav-link{position:absolute;top:54px;font-size:13px;font-weight:600;color:var(--white);white-space:nowrap}
.nav-link.on-light{color:var(--navy)}
.hero-title{left:150px;top:208px;font-size:41px;font-weight:800;color:var(--white)}
.hero-sub{left:150px;top:262px;font-size:33px;font-weight:800;color:transparent;-webkit-text-stroke:1.3px var(--green);letter-spacing:.5px}
.search{left:150px;top:336px;width:402px;height:44px;background:var(--white);display:flex;align-items:center;justify-content:space-between;padding:0 20px 0 22px;font-size:12px;color:#8a95a0}
.photo-frame{left:690px;top:130px;width:360px;height:333px;background:var(--white)}
.hero-photo{left:700px;top:142px;width:350px;height:311px;background:radial-gradient(circle at 45% 45%,#d4382b 0,#8c2a24 25%,#3a3435 55%,#c88a4a 100%)}
/* spec search */
.spec{left:0;top:563px;width:1200px;height:324px;background:linear-gradient(100deg,#1c3d5d 0%,#2d5c5a 55%,#4b9248 100%)}
.sec-title{position:absolute;left:0;width:1200px;text-align:center;font-weight:800}
.rule{position:absolute;display:flex;align-items:center;gap:8px;left:50%;transform:translateX(-50%)}
.rule b{display:block;height:2px;background:var(--green)}
.rule em{width:5px;height:9px;border-radius:3px;background:currentColor;display:block}
.select{position:absolute;height:37px;border:1px solid rgba(255,255,255,.85);color:var(--white);font-size:14px;display:flex;align-items:center;justify-content:space-between;padding:0 20px 0 22px}
.btn{left:544px;top:809px;width:112px;height:39px;background:var(--green);color:var(--white);font-size:13px;font-weight:700;display:flex;align-items:center;justify-content:center}
/* cards */
.arrow{position:absolute;width:38px;height:38px;border-radius:50%;display:flex;align-items:center;justify-content:center;box-shadow:0 4px 14px rgba(0,0,0,.12)}
.arrow.prev{background:var(--white);color:var(--green)}
.arrow.next{background:var(--green);color:var(--white)}
.corner{position:absolute;width:82px;height:82px;background:var(--green)}
.photo{position:absolute;box-shadow:0 8px 24px rgba(0,0,0,.15)}
.artist-name{position:absolute;font-size:22px;font-weight:700;color:var(--navy)}
.artist-role{position:absolute;font-size:14px}
.artist-role span,.accent{color:var(--green)}
.artist-desc{position:absolute;font-size:14px;line-height:22px;width:275px}
.watch{position:absolute;display:flex;align-items:center;gap:24px;font-size:14px}
.play{width:48px;height:48px;border-radius:50%;background:var(--navy);border:4px solid #c9d2da;display:flex;align-items:center;justify-content:center}
.news-title{position:absolute;font-size:22px;font-weight:700;color:var(--navy)}
.news-name{position:absolute;font-size:22px;font-weight:700;color:var(--green)}
/* testimonials */
.testi{left:0;top:2185px;width:1200px;height:751px;background:linear-gradient(160deg,#2c6a57 0%,#3d8a48 40%,#5ea547 70%,#4a8a5a 100%)}
.t-card{position:absolute;background:var(--white);top:2386px;height:195px;font-size:12px;line-height:20px;color:#5b6570;text-align:center}
.t-logo{left:562px;top:2349px;width:74px;height:74px;border-radius:50%;background:var(--white);box-shadow:0 4px 12px rgba(0,0,0,.15);display:flex;align-items:center;justify-content:center;font-size:12px;font-weight:800;color:var(--text)}
.client{position:absolute;top:2826px;font-size:24px;font-weight:800;color:var(--white)}
/* footer */
.footer{left:0;top:2936px;width:1200px;height:222px;background:var(--navy-deep)}
.footer-green{left:803px;top:2936px;width:397px;height:125px;background:var(--green);clip-path:polygon(0 0,100% 0,100% 100%,35px 100%)}
.f-text{position:absolute;color:var(--white);font-size:12px;line-height:27px}
.social{position:absolute;top:3046px;width:27px;height:27px;border-radius:50%;background:var(--white)}
</style>
</head>
<body>

<!-- hero -->
<div class="abs hero-dark"></div>
<div class="abs hero-light"></div>
<div class="abs contact-bar">
  <span style="left:100px"><svg viewBox="0 0 24 24" fill="#1a3a5b"><path d="M6.6 10.8a15 15 0 006.6 6.6l2.2-2.2a1 1 0 011-.25 11.4 11.4 0 003.6.57 1 1 0 011 1V20a1 1 0 01-1 1A17 17 0 013 4a1 1 0 011-1h3.5a1 1 0 011 1c0 1.25.2 2.45.57 3.57a1 1 0 01-.25 1z"/></svg>Sydney: + 61 2 9000 1234</span>
  <span style="left:360px"><svg viewBox="0 0 24 24" fill="#1a3a5b"><path d="M6.6 10.8a15 15 0 006.6 6.6l2.2-2.2a1 1 0 011-.25 11.4 11.4 0 003.6.57 1 1 0 011 1V20a1 1 0 01-1 1A17 17 0 013 4a1 1 0 011-1h3.5a1 1 0 011 1c0 1.25.2 2.45.57 3.57a1 1 0 01-.25 1z"/></svg>Melbourne: + 61 3 9000 5678</span>
</div>
<div class="abs logo" style="left:150px;top:30px">TARNBELLE<i></i></div>
<nav>
  <span class="nav-link" style="left:498px">VOICES</span>
  <span class="nav-link" style="left:570px">RATES</span>
  <span class="nav-link" style="left:634px">PAYMENTS</span>
  <span class="nav-link on-light" style="left:727px">NEWS</span>
  <span class="nav-link on-light" style="left:788px">ABOUT US</span>
  <span class="nav-link on-light" style="left:879px">CONTACT</span>
  <span class="nav-link on-light" style="left:965px">SHORTLIST</span>
</nav>
<h1 class="abs hero-title">Australia’s Top Voices</h1>
<div class="abs hero-sub">PROFESSIONAL CASTING</div>
<div class="abs search">Search Artist
  <svg width="12" height="22" viewBox="0 0 12 22"><rect x="3" y="0" width="6" height="12" rx="3" fill="#7cbb2a"/><rect x="5" y="13" width="2" height="5" fill="#7cbb2a"/><rect x="2" y="18" width="8" height="3" fill="#7cbb2a"/></svg>
</div>
<div class="abs photo-frame"></div>
<div class="abs hero-photo" role="img" aria-label="Close-up photo of a vintage studio microphone with warm bokeh lights"></div>

<!-- search by specification -->
<section class="abs spec" aria-label="Search by specification"></section>
<div class="sec-title" style="top:582px;font-size:21px;color:var(--white)">Search by Specification</div>
<div class="rule" style="top:608px;color:var(--white)"><b style="width:110px;background:#fff"></b><em></em><b style="width:110px;background:#fff"></b></div>
<div class="select" style="left:150px;top:659px;width:274px">Location<svg width="16" height="10"><path d="M1 1l7 7 7-7" stroke="#fff" stroke-width="2" fill="none"/></svg></div>
<div class="select" style="left:462px;top:659px;width:275px">Sex<svg width="16" height="10"><path d="M1 1l7 7 7-7" stroke="#fff" stroke-width="2" fill="none"/></svg></div>
<div class="select" style="left:775px;top:659px;width:275px">Age Range<svg width="16" height="10"><path d="M1 1l7 7 7-7" stroke="#fff" stroke-width="2" fill="none"/></svg></div>
<div class="select" style="left:150px;top:734px;width:274px;padding-left:15px">Talent Range<svg width="16" height="10"><path d="M1 1l7 7 7-7" stroke="#fff" stroke-width="2" fill="none"/></svg></div>
<div class="select" style="left:462px;top:734px;width:275px">Language<svg width="16" height="10"><path d="M1 1l7 7 7-7" stroke="#fff" stroke-width="2" fill="none"/></svg></div>
<div class="select" style="left:775px;top:734px;width:275px">Accent<svg width="16" height="10"><path d="M1 1l7 7 7-7" stroke="#fff" stroke-width="2" fill="none"/></svg></div>
<div class="abs btn">SEARCH</div>

<!-- spotlight -->
<h2 class="sec-title" style="top:930px;font-size:36px;color:var(--navy)">Spotlight</h2>
<div class="rule" style="top:983px;color:var(--navy)"><b style="width:64px"></b><em></em><b style="width:64px"></b></div>
<div class="arrow prev" style="left:59px;top:1159px"><svg width="10" height="14"><path d="M8 1L2 7l6 6" stroke="currentColor" stroke-width="2" fill="none"/></svg></div>
<div class="arrow next" style="left:1101px;top:1159px"><svg width="10" height="14"><path d="M2 1l6 6-6 6" stroke="currentColor" stroke-width="2" fill="none"/></svg></div>

<div class="corner" style="left:135px;top:1043px"></div>
<div class="photo" style="left:150px;top:1058px;width:274px;height:240px;background:linear-gradient(135deg,#8a4a3a,#b27a62 45%,#404850)" role="img" aria-label="Portrait photo of the artist against a brick wall"></div>
<div class="artist-name" style="left:150px;top:1316px">Liam Ashford</div>
<div class="artist-role" style="left:150px;top:1347px">Artist - <span>Sydney</span></div>
<p class="artist-desc" style="left:150px;top:1383px">For his relatively young age. Liam brings a wealth of experience in every session.</p>
<div class="watch" style="left:150px;top:1446px"><div class="play"><svg width="12" height="14"><path d="M0 0l12 7-12 7z" fill="#7cbb2a"/></svg></div>Watch Video</div>

<div class="corner" style="left:662px;top:1269px"></div>
<div class="photo" style="left:455px;top:1097px;width:274px;height:239px;background:linear-gradient(135deg,#f3efe9,#d7b49a 50%,#8a5a3e)" role="img" aria-label="Portrait photo of the artist smiling"></div>
<div class="artist-name" style="left:455px;top:1369px">Nina Caldwell</div>
<div class="artist-role" style="left:455px;top:1400px">Artist - <span>Sydney</span></div>
<p class="artist-desc" style="left:455px;top:1436px">Nina Caldwell is a great young emerging voice and a passionate actress and completed course of the Harbour Drama School, a masterclass with Jane Whitlow.</p>
<div class="watch" style="left:455px;top:1545px"><div class="play"><svg width="12" height="14"><path d="M0 0l12 7-12 7z" fill="#7cbb2a"/></svg></div>Watch Video</div>

<div class="corner" style="left:983px;top:1043px"></div>
<div class="photo" style="left:775px;top:1058px;width:275px;height:240px;background:linear-gradient(135deg,#2b2b2e,#6b5547 50%,#1d1d20)" role="img" aria-label="Portrait photo of the artist in a dark jacket"></div>
<div class="artist-name" style="left:775px;top:1316px">Owen Marsh</div>
<div class="artist-role" style="left:775px;top:1347px">Artist - <span>Sydney</span></div>
<p class="artist-desc" style="left:775px;top:1383px">Owen knows how to make a read connect with the with the listener with his warm, conversational &amp; intelligent voice.</p>
<div class="watch" style="left:775px;top:1468px"><div class="play"><svg width="12" height="14"><path d="M0 0l12 7-12 7z" fill="#7cbb2a"/></svg></div>Watch Video</div>

<!-- news -->
<h2 class="sec-title" style="top:1662px;font-size:36px;color:var(--navy)">News</h2>
<div class="rule" style="top:1715px;color:var(--navy)"><b style="width:34px"></b><em></em><b style="width:34px"></b></div>
<div class="arrow prev" style="left:59px;top:1892px"><svg width="10" height="14"><path d="M8 1L2 7l6 6" stroke="currentColor" stroke-width="2" fill="none"/></svg></div>
<div class="arrow next" style="left:1101px;top:1892px"><svg width="10" height="14"><path d="M2 1l6 6-6 6" stroke="currentColor" stroke-width="2" fill="none"/></svg></div>

<div class="corner" style="left:135px;top:1777px"></div>
<div class="photo" style="left:150px;top:1792px;width:431px;height:239px;background:linear-gradient(90deg,#5a5a5a,#cfcfcf 30%,#4a4a4a 50%,#d0d0d0 70%,#555)" role="img" aria-label="Black and white headshot strip of the new voice artist"></div>
<div class="news-title" style="left:150px;top:2050px">New Voice Alert</div>
<div class="news-name" style="left:150px;top:2084px">Felix Orman</div>

<div class="corner" style="left:983px;top:1964px"></div>
<div class="photo" style="left:619px;top:1792px;width:431px;height:239px;background:linear-gradient(90deg,#3e3a36,#b7a898 30%,#3a3632 50%,#bbad9e 70%,#3c3834)" role="img" aria-label="Sepia headshot strip of the new voice artist"></div>
<div class="news-title" style="left:619px;top:2050px">New Voice Alert</div>
<div class="news-name" style="left:619px;top:2084px">Hugo Barnett</div>

<!-- testimonials and clients -->
<section class="abs testi" aria-label="Testimonials and clients"></section>
<h2 class="sec-title" style="top:2230px;font-size:36px;color:var(--white)">Testimonials</h2>
<div class="rule" style="top:2283px;color:var(--white)"><b style="width:98px"></b><em></em><b style="width:98px"></b></div>

<div class="t-card" style="left:0;width:267px;padding:42px 20px 0 0;text-align:right">consetetur sadipscing elitr, sed diam<br>ut labore et dolore magna aliquyam<br>eos et accusam et justo duo dolores<br>rebum, no sea takimata sanctus est<br>dolor sit amet.</div>
<div class="t-card" style="left:928px;width:272px;padding:42px 0 0 50px;text-align:left">Lorem ipsum dolor sit amet, conse<br>nonumy eirmod tempor invidunt ut la<br>erat, sed diam voluptua. At vero eos e<br>et ea rebum. Stet clita kasd guberg<br>Lorem ipsum dolo</div>
<div class="t-card" style="left:343px;width:510px;padding-top:60px;font-size:12.5px">I’ve been working for the team of Tarnbelle now for almost<br>11 years and I’ve always found them to be very<br>professional and personable in all jobs.
  <div style="margin-top:18px;color:var(--green);font-weight:700">Brightwell</div>
  <div style="font-size:11px;line-height:14px;color:#9aa3ab">Sam Ellery, National Head of Broadcast</div>
</div>
<div class="abs t-logo">Brightwell</div>
<div class="arrow prev" style="left:324px;top:2465px"><svg width="10" height="14"><path d="M8 1L2 7l6 6" stroke="currentColor" stroke-width="2" fill="none"/></svg></div>
<div class="arrow next" style="left:834px;top:2465px"><svg width="10" height="14"><path d="M2 1l6 6-6 6" stroke="currentColor" stroke-width="2" fill="none"/></svg></div>
<svg class="abs" style="left:578px;top:2632px" width="40" height="8"><circle cx="4" cy="4" r="3.5" fill="#7cbb2a"/><circle cx="20" cy="4" r="3.5" fill="#fff" opacity=".6"/><circle cx="36" cy="4" r="3.5" fill="#fff" opacity=".6"/></svg>

<h2 class="sec-title" style="top:2708px;font-size:36px;color:var(--white)">Clients</h2>
<div class="rule" style="top:2761px;color:var(--white)"><b style="width:48px"></b><em></em><b style="width:48px"></b></div>
<div class="arrow prev" style="left:57px;top:2823px"><svg width="10" height="14"><path d="M8 1L2 7l6 6" stroke="currentColor" stroke-width="2" fill="none"/></svg></div>
<div class="arrow next" style="left:1099px;top:2823px"><svg width="10" height="14"><path d="M2 1l6 6-6 6" stroke="currentColor" stroke-width="2" fill="none"/></svg></div>
<div class="client" style="left:152px">Northline Media</div>
<div class="client" style="left:480px;font-size:16px;top:2832px">Pulse FM</div>
<div class="client" style="left:690px;font-size:20px;top:2829px">Fastplay</div>
<div class="client" style="left:935px">Vistacast</div>

<!-- footer -->
<footer class="abs footer"></footer>
<div class="abs footer-green"></div>
<div class="abs logo" style="left:150px;top:2997px">TARNBELLE<i></i></div>
<div class="social" style="left:150px" aria-label="Social link"></div>
<div class="social" style="left:188px" aria-label="Social link"></div>
<div class="social" style="left:226px" aria-label="Social link"></div>
<div class="social" style="left:264px" aria-label="Social link"></div>
<div class="f-text" style="left:368px;top:2981px">Tarnbelle Pty Limited<br>Suite 14, 90 Harbour Rd Northgate<br>NSW 2099 Australia</div>
<div class="f-text" style="left:662px;top:2981px">Privacy Policy<br>Terms and Conditions<br>Sitemap</div>
<div class="f-text" style="left:856px;top:2981px;line-height:39px">
  <div style="display:flex;align-items:center;gap:10px"><svg width="15" height="15" viewBox="0 0 24 24" fill="#fff"><path d="M6.6 10.8a15 15 0 006.6 6.6l2.2-2.2a1 1 0 011-.25 11.4 11.4 0 003.6.57 1 1 0 011 1V20a1 1 0 01-1 1A17 17 0 013 4a1 1 0 011-1h3.5a1 1 0 011 1c0 1.25.2 2.45.57 3.57a1 1 0 01-.25 1z"/></svg>Sydney: + 61 2 9000 1234</div>
  <div style="display:flex;align-items:center;gap:10px"><svg width="15" height="15" viewBox="0 0 24 24" fill="#fff"><path d="M6.6 10.8a15 15 0 006.6 6.6l2.2-2.2a1 1 0 011-.25 11.4 11.4 0 003.6.57 1 1 0 011 1V20a1 1 0 01-1 1A17 17 0 013 4a1 1 0 011-1h3.5a1 1 0 011 1c0 1.25.2 2.45.57 3.57a1 1 0 01-.25 1z"/></svg>Melbourne: + 61 3 9000 5678</div>
</div>
<div class="abs" style="left:150px;top:3111px;width:900px;height:1px;background:rgba(255,255,255,.25)"></div>
<div class="abs" style="left:0;top:3126px;width:1200px;text-align:center;color:var(--white);font-size:12px">© Copyright 2018 Tarnbelle Pty Limited.</div>

</body>
</html>
```